VornaFlex™ (the "Brelka of mind/body fitness") needs a new web design!

Ever heard of Dov Ramsel? Yes - the international martial arts movie star! I am Dov's American partner, and our company is on a mission to promote Taiji (Tai Chi) worldwide. If you would like to start a relationship with our company, please take a shot at this project. By the way, this is our first attempt at using crowd-sourcing so we are being a little conservative. But if this works we will definitely be doing more and bigger projects.

I need a re-design of my website. (www.vornaflex.net) I am currently using Wordpress because it allows us lots of flexibility and is easy for my non-tech staff to update when needed. We don't use it for blogging, by the way.

We are called VornaFlex - a modern taiji (tai chi)-based workout. It is designed to make Taiji more enjoyable and accessible and help people experience the essence of Taiji immediately. It's also a great fitness workout - and most of all it is hip and fun.

We are basically re-branding Taiji into Western culture - "it's not your Grand-dad's Taiji!" The website has to communicate all of this to both consumers (the people who will take the classes) and to fitness professionals who will take our teacher training course.

I'm sure all of this will make more sense when you look at the current website. However, the current website doesn't have much punch - it doesn't convey the energy we want to get across, and it's really confusing to navigate besides.
Updates

Project Deadline Extended
Reason: First of all - thanks to the designers who have submitted designs. Several of them have been excellent and are still on the top of our consideration list. However, the response from the list of designers that we invited was really slow to start, and we did not recieve that many ideas. Secondly, I have been traveling so much the last two weeks that I was not able to provide as much feedback as I intended. I'd like to see if giving this just a few more days will finally bring out the design we're looking for.

Target Market(s)

Primary Target Market: female fitness professional with mind/body interest, 35-45 y/o; 5+ years in fitness

Industry/Entity Type

Fitness

Requirements
Must have
• Have to weave in the use of our logo, and also we like use of imagery. We're working on a video sizzle reel that we will want to feature on the site as soon as it's done.

The site also integrates ticketplume as our e-commerce tool to register people for our teacher training workshops and retreats.

We want a site that is clean, uncluttered and easy to navigate.

```html
<!DOCTYPE html>
<html lang="en">
<head>
<meta charset="utf-8">
<title>VornaFlex™ – A Revolution in Mind/Body Exercise</title>
<link href="https://fonts.googleapis.com/css2?family=Fjalla+One&family=Archivo+Black&family=Open+Sans:wght@400;600&display=swap" rel="stylesheet">
<style>
:root{
  --red:#d42a3a;
  --red-dark:#a81d2a;
  --yellow:#f6eb8c;
  --ink:#222;
  --text:#333;
  --footer:#2b2b2b;
  --footer-deep:#1b1b1b;
  --footer-text:#777;
  --footer-head:#ddd;
  --white:#fff;
}
*{box-sizing:border-box;margin:0;padding:0}
html,body{width:1052px;height:1200px;overflow:hidden}
body{position:relative;background:var(--white);font-family:Arial,Helvetica,sans-serif;color:var(--text)}
.abs{position:absolute}
.header{top:0;left:0;width:1052px;height:120px;background:linear-gradient(#e9e9e9,#fff 60%)}
.brand{left:150px;top:22px;display:flex;align-items:center;gap:10px}
.brand-dot{width:34px;height:34px;border-radius:50%;background:var(--red)}
.brand-name{font-family:"Fjalla One",sans-serif;font-size:40px;color:var(--red)}
.tagline{left:130px;top:98px;font-size:12px;color:var(--ink)}
.social{left:694px;top:30px;display:flex;gap:6px}
.social span{width:34px;height:34px;border-radius:4px;background:var(--red)}
.social span:nth-child(odd){background:#5a6e8c}
.search{left:761px;top:79px;width:173px;height:27px;border:1px solid #ccc;border-radius:4px;background:#fff;font-size:11px;padding:7px 9px;color:#333}
.search svg{position:absolute;right:8px;top:5px}
.nav{top:122px;left:0;width:1052px;height:44px;background:var(--red);border-top:3px solid var(--yellow);border-bottom:3px solid var(--red-dark)}
.nav a{position:absolute;top:0;height:38px;line-height:38px;font-family:"Fjalla One",sans-serif;font-size:17px;color:var(--white);text-decoration:none;white-space:nowrap}
.nav a.active{background:var(--yellow);color:var(--ink);padding:0 12px;border-radius:4px 4px 0 0;top:3px;height:35px;line-height:35px}
.stage{top:166px;left:0;width:1052px;height:512px;background:linear-gradient(#9e9e9e,#d8d8d8 60%,#f4f4f4)}
.hero{left:119px;top:179px;width:815px;height:318px;border:4px solid var(--white);background:linear-gradient(120deg,#6e6258,#8b7a6a 45%,#4a3d34);box-shadow:0 1px 4px rgba(0,0,0,.3)}
.hero-card{left:650px;top:200px;width:262px;height:274px}
.card-brand{left:684px;top:216px;width:228px;display:flex;align-items:center;justify-content:center;gap:6px;font-family:"Fjalla One",sans-serif;font-size:14px;color:var(--red);white-space:nowrap}
.card-brand i{width:16px;height:16px;border-radius:50%;background:var(--red)}
.card-lines{left:684px;top:274px;width:228px;text-align:center;font-family:"Open Sans",sans-serif;font-size:11.5px;line-height:19.5px;color:var(--ink);white-space:nowrap}
.card-lines b{font-weight:600}
.card-lines .hot{color:var(--red)}
.master{left:684px;top:388px;width:228px;text-align:center;font-family:"Archivo Black",sans-serif;font-size:29px;line-height:31px;letter-spacing:-1px;color:#111}
.master span{color:var(--red)}
.teaser{top:516px;width:256px;height:142px;background:var(--white);border:1px solid #ccc;box-shadow:0 1px 3px rgba(0,0,0,.12)}
.teaser svg{position:absolute;left:0;top:0}
.teaser h3{position:absolute;left:12px;top:8px;display:flex;align-items:center;gap:9px;font-family:"Fjalla One",sans-serif;font-weight:400;font-size:24px;color:var(--white)}
.teaser h3 i{width:26px;height:26px;border-radius:50%;background:var(--yellow)}
.teaser p{position:absolute;left:12px;top:64px;width:232px;font-size:11.3px;line-height:14px;color:var(--text)}
.teaser p em{font-style:normal;color:var(--red)}
.teaser a{position:absolute;left:12px;top:112px;font-size:12px;color:#111;text-decoration:underline}
.rule{top:676px;left:118px;width:816px;height:1px;background:#e4e4e4}
.section-title{font-family:"Fjalla One",sans-serif;font-size:24px;color:var(--ink);font-weight:400}
.about{left:118px;top:702px;width:534px}
.about p{font-size:11.6px;line-height:14.5px;margin-top:17px;color:var(--text)}
.about p:first-of-type{margin-top:24px}
.divider{left:667px;top:702px;width:1px;height:226px;background:#ddd}
.news{left:694px;top:702px;width:240px}
.news-item{border-bottom:1px solid #ddd;padding-bottom:8px}
.news-item:first-of-type{margin-top:20px}
.news-item + .news-item{margin-top:12px;border:0}
.news time{display:block;font-size:12px;color:var(--red)}
.news p{font-size:11.5px;line-height:14px}
.news a{display:inline-block;margin-top:12px;font-size:12px;color:var(--red)}
.footer{top:948px;left:0;width:1052px;height:216px;background:var(--footer);border-top:4px solid var(--red-dark)}
.copyright{top:1164px;left:0;width:1052px;height:36px;background:var(--footer-deep);text-align:center;font-size:11px;line-height:36px;color:#888}
.col{top:964px}
.col h4{font-family:"Fjalla One",sans-serif;font-weight:400;font-size:21px;color:var(--footer-head)}
.links{left:118px}
.links li{list-style:none;font-size:11.5px;line-height:19px;color:var(--footer-text)}
.links ul{margin-top:10px}
.join{left:253px;width:200px}
.join p{margin-top:12px;font-size:11.5px;line-height:14px;color:var(--footer-text)}
.join .field{margin-top:10px;width:196px;height:20px;background:#eee;font-size:11px;padding:3px 8px;color:#222}
.join .field + .field{margin-top:10px}
.join .submit{display:inline-block;margin-top:14px;padding:3px 10px;border:2px solid #ddd;border-radius:3px;background:var(--red);font-family:"Archivo Black",sans-serif;font-size:12px;letter-spacing:1px;color:#fff}
.experience{left:490px;width:230px}
.quote{position:relative;margin-top:12px;width:226px;height:90px;border-radius:8px;background:#e6e6e6;padding:8px 10px;font-style:italic;font-size:12.5px;line-height:15px;color:#222}
.quote svg{position:absolute;left:174px;bottom:-14px}
.cite{margin-top:22px;text-align:right;font-style:italic;font-size:13px;color:var(--red)}
.contact{left:757px;width:180px}
.contact address{margin-top:12px;font-style:normal;font-size:11.5px;line-height:14px;color:var(--footer-text)}
.contact p{margin-top:12px;font-size:11.5px;color:#eee}
.contact p + p{margin-top:6px}
.contact p span{color:var(--red)}
</style>
</head>
<body>

<header class="abs header">
  <div class="abs brand"><i class="brand-dot"></i><span class="brand-name">VornaFlex</span></div>
  <div class="abs tagline">A Revolution in mind/Body Exercise</div>
  <div class="abs social" aria-label="Social links"><span></span><span></span><span></span><span></span><span></span><span></span></div>
  <div class="abs search">Enter keyword here
    <svg width="18" height="18" viewBox="0 0 18 18"><circle cx="7" cy="7" r="5" fill="none" stroke="#777" stroke-width="2"/><line x1="11" y1="11" x2="16" y2="16" stroke="#777" stroke-width="3"/></svg>
  </div>
</header>

<nav class="abs nav">
  <a class="active" style="left:138px">Home</a>
  <a style="left:227px">Find a Class</a>
  <a style="left:341px">Instructor Training</a>
  <a style="left:503px">VornaFlex Retreat</a>
  <a style="left:646px">Meet RKV</a>
  <a style="left:739px">Contact</a>
  <a style="left:828px">About</a>
</nav>

<div class="abs stage" role="img" aria-label="Faded photo of a class moving together in a studio"></div>

<div class="abs hero" role="img" aria-label="Photo of an instructor leading a class with arms extended"></div>
<svg class="abs hero-card" width="262" height="274" viewBox="0 0 262 274">
  <path d="M22 0H262V274H26C36 240 18 210 24 180C30 150 8 120 10 90C12 60 2 30 22 0Z" fill="#fff"/>
</svg>
<div class="abs card-brand"><i></i>VornaFlex Instructor Training</div>
<div class="abs card-lines">
  <b>POWERFUL</b> Incredible <b>LIFE CHANGING</b><br>
  I Cried more than I expected Blew my<br>
  Mind Wow it will Change Fitness<br>
  <span class="hot">BEST WORKOUT EVER</span><br>
  Floating Dancing Flying
</div>
<div class="abs master">master<br>the <span>FLOW</span></div>

<div class="abs teaser" style="left:118px">
  <svg width="256" height="56" viewBox="0 0 256 56"><path d="M0 0H256V48C190 34 80 60 0 40Z" fill="var(--red)"/></svg>
  <h3><i></i>Find an Event</h3>
  <p><em>VornaFlex™</em> is a special kind of movement experience that meets all your fitness needs… and more. It's more than just an exercise.</p>
  <a>Learn more&gt;&gt;</a>
</div>
<div class="abs teaser" style="left:397px">
  <svg width="256" height="56" viewBox="0 0 256 56"><path d="M0 0H256V48C190 34 80 60 0 40Z" fill="var(--red)"/></svg>
  <h3><i></i>Find a Training</h3>
  <p><em>Are you a fitness professional?</em> Earn CECs and get certified by the most respected T'ai Chi teacher training program...</p>
  <a>Learn more&gt;&gt;</a>
</div>
<div class="abs teaser" style="left:678px">
  <svg width="256" height="56" viewBox="0 0 256 56"><path d="M0 0H256V48C190 34 80 60 0 40Z" fill="var(--red)"/></svg>
  <h3><i></i>Find a Teacher</h3>
  <p><em>VornaFlex™</em> classes are popping up all over the country, as more and more instructors graduate from our program.</p>
  <a>Find a Class &gt;&gt;</a>
</div>

<div class="abs rule"></div>

<section class="abs about">
  <h2 class="section-title">What is VornaFlex™?</h2>
  <p>Imagine… to the rhythm of modern music, a roomful of people glide and sway across the floor – bodies pulsing with Qi, while muscles, mind and breath come together as One.</p>
  <p>That's the VornaFlex™ Experience.</p>
  <p>VornaFlex™ is a mind/body "exercise" that combines the best of traditional Taiji (Tai Chi) with modern Western fitness. It's a workout appropriate for any age or fitness level – and has you experiencing the FLOW of Taiji whether it's your first class or 100th. There are no routines to learn, or set choreography to remember. Instead, class members follow an instructor trained in a method known as "Qi Cueing" – designed to bring your muscular, cardiovascular and nervous systems into perfect synergy (along with your mind and Spirit). It finally makes Taiji accessible to everyone.</p>
</section>

<div class="abs divider"></div>

<section class="abs news">
  <h2 class="section-title">Recent News</h2>
  <div class="news-item">
    <time>June 26, 2013</time>
    <p>VornaFlex has invaded China! Last night Ronan-Kell brought the first-ever VornaFlex Experience to Beijing fitness enthusiasts.</p>
  </div>
  <div class="news-item">
    <time>May 29, 2013</time>
    <p>VornaFlex has landed in Europe! Lia Ostrand will be teaching a VornaFlex Experience class at Halden Fitness Haus Saarbrüken Germany.</p>
  </div>
  <a>View All&gt;&gt;</a>
</section>

<footer class="abs footer"></footer>

<div class="abs col links">
  <h4>Quick Links</h4>
  <ul><li>Home</li><li>Find a Class</li><li>Instructor Training</li><li>VornaFlex Retreat</li><li>Meet RKV</li><li>Contact</li></ul>
</div>
<div class="abs col join">
  <h4>Join us</h4>
  <p>Please enter your name and Email address below to get our newsletter.</p>
  <div class="field">Your name</div>
  <div class="field">Email Address</div>
  <span class="submit">SUBMIT</span>
</div>
<div class="abs col experience">
  <h4>The VornaFlex Experience</h4>
  <div class="quote">"My Mom stood up and took the class - and she doesn't stand up for anything!"
    <svg width="24" height="16" viewBox="0 0 24 16"><path d="M0 0H24L14 16Z" fill="#e6e6e6"/></svg>
  </div>
  <div class="cite">Nell T. Orwin</div>
</div>
<div class="abs col contact">
  <h4>Contact Info</h4>
  <address>Building No.123<br>Dummy Street<br>Dummy state, United states.</address>
  <p><span>Email- </span>hello@vornaflex.net</p>
  <p><span>Call us- </span>0980-555-014</p>
</div>

<div class="abs copyright">Copyright 2013 vornaflex.net &nbsp;All Rights Reserved.</div>

</body>
</html>
```